Business Card Design

I do estate sales and would like business card to reflect look and feel of attached logo. I also have copy of logo in .eps and .tif if you need that instead of .jpeg.
Updates

sorry for the delay in reviewing these designs. I will pick one by tomorrow. Here are the absolutes: *must have tagline (we find good homes for your treasures *must use blue and green *must be horizontal *nothing too fancy please submit your best and final. Thanks so much!

Industry/Entity Type

Business

Contact Information for Business Card

Mira Tolland

TAGS by MIRA
We find good homes for your treasures.

Specializing in one to three-day sales
o (no sale too big or too small)
• Home and garage organizing
• Home Clean-out

Call Mira Tolland at 202-555-0147
to schedule.

```html
<!DOCTYPE html>
<html lang="en">
<head>
<meta charset="utf-8">
<title>TAGS by MIRA – Business Card</title>
<link rel="stylesheet" href="https://fonts.googleapis.com/css2?family=Roboto:wght@400;900&family=Indie+Flower&display=swap">
<style>
  :root {
    --page: #e6e6e2;
    --card-white: #fbfbf9;
    --leaf-green: #5b7526;
    --ink-green: #5f7a22;
    --sea-blue: #1d6f90;
    --deep-blue: #134f68;
    --text-light: #ffffff;
  }
  * { margin: 0; padding: 0; box-sizing: border-box; }
  html, body {
    width: 1200px; height: 1000px; overflow: hidden;
    background: var(--page);
  }
  .business-card {
    position: absolute; left: 75px; top: 200px;
    width: 1050px; height: 600px;
    border-radius: 6px; overflow: hidden;
    box-shadow: 0 12px 30px rgba(0,0,0,0.22);
    font-family: "Roboto", Arial, sans-serif;
  }
  .card-backdrop { position: absolute; inset: 0; }
  .wordmark {
    position: absolute; left: 70px; top: 28px;
    color: var(--leaf-green);
    font-family: "Roboto", Arial, sans-serif;
    font-weight: 400; line-height: 0.95; text-align: center;
  }
  .wordmark .big { display: block; font-size: 70px; letter-spacing: 2px; }
  .wordmark .small { display: block; font-size: 34px; }
  .tagline {
    position: absolute; left: 470px; top: 125px;
    font-family: "Indie Flower", cursive;
    font-size: 50px; line-height: 1.1; color: var(--ink-green);
  }
  .tagline .line-two { display: block; padding-left: 36px; }
  .tagline .accent { color: var(--sea-blue); }
  .specialty-banner {
    position: absolute; left: 50px; top: 300px;
    width: 960px; height: 66px;
    background: var(--sea-blue); border-radius: 33px;
    box-shadow: 0 12px 0 var(--deep-blue);
    color: var(--text-light);
    font-weight: 900; font-size: 30px; letter-spacing: 1.5px;
    display: flex; align-items: center; justify-content: space-between;
    padding: 0 30px;
  }
  .specialty-banner .star { font-size: 24px; }
  .service-list {
    position: absolute; left: 90px; top: 410px;
    list-style: disc; color: var(--text-light);
    font-size: 30px; line-height: 1.3;
  }
  .contact-line {
    position: absolute; left: 640px; top: 470px;
    color: var(--text-light); font-size: 30px; line-height: 1.3;
  }
</style>
</head>
<body>
  <div class="business-card">
    <svg class="card-backdrop" width="1050" height="600" viewBox="0 0 1050 600" aria-hidden="true">
      <rect width="1050" height="600" fill="var(--card-white)"/>
      <path d="M0,230 L1000,300 Q1050,304 1050,254 L1050,600 L0,600 Z" fill="var(--leaf-green)"/>
    </svg>

    <div class="wordmark">
      <span class="big">TAGS</span>
      <span class="small">by</span>
      <span class="big">MIRA</span>
    </div>

    <p class="tagline">We find good homes<span class="line-two">for <span class="accent">your treasures</span></span></p>

    <div class="specialty-banner">
      <span class="star">★</span>
      <span>SPECIALIZING IN ONE TO THREE-DAY SALES</span>
      <span class="star">★</span>
    </div>

    <ul class="service-list">
      <li>Home &amp; garage organizing</li>
      <li>Home Clean-out</li>
    </ul>

    <p class="contact-line">Call Mira Tolland at<br>202-555-0147 to schedule.</p>
  </div>
</body>
</html>
```